Capability statement graphic design documement

We have written a capability statement for our training business, we would like someone to really make it professional and stand out.

Target Market(s)

Engineering, ports and mining companies

Industry/Entity Type

Coal Mining

Font styles to use
Sans Serif

Colors
9bcb3c

Requirements
Must have
• Very good visual designs.
I have included a couple of example such as the Orvo Dune capability statement which has good designs.
Our colours are green, black, white, grey. Our logos are uploaded.

```html
<!DOCTYPE html>
<html lang="en">
<head>
<meta charset="utf-8">
<title>KVTR Capability Statement – Key Personnel</title>
<link href="https://fonts.googleapis.com/css2?family=Source+Sans+3:wght@400;500&display=swap" rel="stylesheet">
<style>
  :root {
    --brand-green: #6fa853;
    --tint-green: #e1ecdc;
    --rock-dark: #8f918f;
    --rock-light: #d9dad8;
    --card: #f8f8f6;
    --ink: #4a4a4a;
    --ink-soft: #5a5a5a;
    --paper: #ffffff;
  }
  * { margin: 0; padding: 0; box-sizing: border-box; }
  html, body { width: 849px; height: 1200px; overflow: hidden; background: var(--paper); }
  body { font-family: "Source Sans 3", sans-serif; color: var(--ink-soft); }
  .page { position: relative; width: 849px; height: 1200px; overflow: hidden; background: var(--paper); }
  .backdrop { position: absolute; inset: 0; }
  .title-band { position: absolute; left: 0; top: 44px; }
  .page-title {
    position: absolute; left: 21px; top: 50px;
    font-size: 37px; font-weight: 400; color: var(--paper); letter-spacing: 0.2px; line-height: 1;
  }
  .portrait-panel { position: absolute; left: 0; top: 171px; width: 400px; height: 259px; background: var(--brand-green); }
  .portrait {
    position: absolute; left: 188px; top: 194px; width: 186px; height: 213px;
    border: 1.5px solid #fff; box-shadow: 3px 4px 8px rgba(0,0,0,0.3);
    background: linear-gradient(180deg, #e4e2de 0%, #d9c3ab 45%, #e98a2e 72%, #e57c22 100%);
  }
  .abs { position: absolute; }
  .person-name { left: 452px; top: 190px; font-size: 25px; color: var(--ink); font-weight: 400; line-height: 1.1; }
  .person-role { left: 452px; top: 220px; font-size: 20px; color: var(--ink); line-height: 1.1; }
  .section-heading {
    font-size: 20px; font-weight: 400; color: var(--ink); line-height: 1.1;
    padding-bottom: 2px; display: inline-block; position: relative;
  }
  .section-heading::after {
    content: ""; position: absolute; left: 0; bottom: -2px; width: 80px; height: 1.5px; background: var(--brand-green);
  }
  .body-copy { font-size: 15.3px; line-height: 20px; text-align: justify; color: var(--ink-soft); }
  .responsibilities { left: 452px; top: 277px; width: 352px; }
  .responsibilities .body-copy { margin-top: 14px; }
  .responsibilities .body-copy + .body-copy { margin-top: 20px; }
  .bullet-list { list-style: none; margin-top: 12px; }
  .bullet-list li { position: relative; padding-left: 16px; font-size: 15.3px; line-height: 20.5px; text-align: justify; }
  .bullet-list li::before {
    content: ""; position: absolute; left: 2px; top: 9px; width: 3px; height: 3px; border-radius: 50%; background: var(--brand-green);
  }
  .strengths { left: 44px; top: 466px; width: 356px; }
  .qualifications { left: 452px; top: 466px; width: 370px; }
  .experience { left: 44px; top: 643px; width: 524px; }
  .experience .body-copy { margin-top: 12px; }
  .role-card { position: absolute; width: 408px; height: 151px; background: var(--card); }
  .role-card .employer { position: absolute; top: 14px; font-size: 16.5px; color: var(--ink); line-height: 1.1; }
  .role-card .position { position: absolute; top: 34px; font-size: 15px; color: var(--ink-soft); line-height: 1.1; }
  .role-card .bullet-list { position: absolute; top: 63px; margin: 0; width: 340px; }
  .role-card .bullet-list li { font-size: 15.3px; line-height: 19px; }
  .card-left { left: 0; }
  .card-left .employer, .card-left .position { left: 44px; }
  .card-left .bullet-list { left: 44px; }
  .card-right { left: 442px; width: 407px; }
  .card-right .employer, .card-right .position { left: 23px; }
  .card-right .bullet-list { left: 23px; width: 350px; }
  .page-tab { position: absolute; left: 0; top: 1117px; width: 99px; height: 19px; background: var(--brand-green); }
  .page-number { position: absolute; left: 83px; top: 1118px; font-size: 11px; color: var(--ink); }
  .footer-rule { position: absolute; left: 20px; top: 1157px; width: 215px; height: 1px; background: var(--brand-green); }
  .footer-label { position: absolute; left: 20px; top: 1158px; font-size: 11px; color: var(--brand-green); }
</style>
</head>
<body>
<main class="page">
  <svg class="backdrop" width="849" height="1200" viewBox="0 0 849 1200" aria-hidden="true">
    <defs>
      <linearGradient id="rock" x1="0" y1="0" x2="0.4" y2="1">
        <stop offset="0" stop-color="#e6e7e5"/>
        <stop offset="0.5" stop-color="#b9bbb9"/>
        <stop offset="1" stop-color="#a4a6a4"/>
      </linearGradient>
    </defs>
    <polygon points="0,533 442,753 0,753" fill="var(--tint-green)"/>
    <polygon points="849,0 849,1200 606,1200 566,1075 0,1075 0,900 408,760 468,748 837,16" fill="url(#rock)"/>
    <polygon points="530,748 849,640 849,748" fill="var(--tint-green)"/>
    <polygon points="567,1077 789,1077 606,1200" fill="var(--tint-green)"/>
  </svg>
  <div class="backdrop" role="img" aria-label="Faded photograph of coal rock texture behind the right side of the page" style="pointer-events:none"></div>

  <svg class="title-band" width="505" height="54" viewBox="0 0 505 54" aria-hidden="true">
    <polygon points="0,0 452,0 505,54 0,54" fill="var(--brand-green)"/>
  </svg>
  <h1 class="page-title">KEY PERSONNEL</h1>

  <div class="portrait-panel"></div>
  <div class="portrait" role="img" aria-label="Portrait photo of Tessa Marlow in orange hi-vis work shirt"></div>

  <h2 class="abs person-name">TESSA MARLOW</h2>
  <p class="abs person-role">Director / Business Manager</p>

  <section class="abs responsibilities">
    <h3 class="section-heading">Key Responsibilities</h3>
    <p class="body-copy">Tessa drives the overall direction of the business focusing on building relationships and networks within the industry.</p>
    <p class="body-copy">Tessa manages all aspects of administration, finances, legislative requirements, and marketing.</p>
  </section>

  <section class="abs strengths">
    <h3 class="section-heading">Personal Strengths</h3>
    <ul class="bullet-list">
      <li>Strong communication and interpersonal skills</li>
      <li>Always has time to invest in others</li>
      <li>Logical and systematic</li>
      <li>Good understanding of training required for mining, ports and civil industries</li>
    </ul>
  </section>

  <section class="abs qualifications">
    <h3 class="section-heading">Qualifications</h3>
    <ul class="bullet-list">
      <li>Bachelor of Business (Coastal Ridge University)</li>
      <li>Graduate Certificate in Learning Technology</li>
      <li>Graduate Diploma in Secondary Education</li>
      <li>Diploma in OHS</li>
      <li>Certificate IV in TAE</li>
    </ul>
  </section>

  <section class="abs experience">
    <h3 class="section-heading">Experience</h3>
    <p class="body-copy">Some of Tessa’s recent experience in her 12 years in education and learning and development:</p>
  </section>

  <article class="role-card card-left" style="top:748px">
    <h4 class="employer">HARROW POINT COAL TERMINAL</h4>
    <p class="position">Training Officer</p>
    <ul class="bullet-list">
      <li>Seconded into Training Advisor position to coordinate the training requirements for Business Services/Business Improvement</li>
    </ul>
  </article>

  <article class="role-card card-right" style="top:748px">
    <h4 class="employer">KESTREL RANGE’S ASHFORD CREEK MINE</h4>
    <p class="position">Training Coordinator</p>
    <ul class="bullet-list">
      <li>Part of a team who designed a site-wide Training Needs Analysis and online document library</li>
      <li>Managed the training requirements for the Maintenance and CHPP departments</li>
    </ul>
  </article>

  <article class="role-card card-left" style="top:924px">
    <h4 class="employer">VERITAN AUSTRALIA</h4>
    <p class="position">Trainer</p>
    <ul class="bullet-list">
      <li>Part of a team who designed the initial 3-day Standard 11 course</li>
      <li>Delivered generic induction training across Queensland</li>
    </ul>
  </article>

  <article class="role-card card-right" style="top:924px">
    <h4 class="employer">STATE LEARNING DEPARTMENT</h4>
    <p class="position">Secondary School Teacher</p>
  </article>

  <div class="page-tab"></div>
  <span class="page-number">5</span>
  <div class="footer-rule"></div>
  <span class="footer-label">KVTR Capability Statement</span>
</main>
</body>
</html>
```